Commercial Real Estate Executive Recruiting Firm Needs Business Card Design

We need a business card design for BRAMLEY | Executive Recruiting - an executive recruiting firm focused exclusively on the commercial real estate industry. We place professionals ranging from Analyst to the Executive Office covering all investment/finance disciplines (acquisitions, asset management, capital markets, etc.) in all product types (office, retail, multifamily, industrial, land, etc.). We have a passion for helping people (clients and candidates) and have a reputation for being open and honest in our recruiting - and yes, very successful. We have recently developed a new logo and would like to update our business cards as well. I've uploaded some information about our company that contains the new logo.

Target Market(s)

Commercial Real Estate professionals. Primarily in the US. These are typically, smart, driven professionals with finance degrees and MBAs. Primarily men between the ages of 25 and 55.

Industry/Entity Type

Real Estate

Font styles to use
Other font styles liked:
• The font for "BRAMLEY" is Blair ITC (Medium), and "executive recruiting" is Gotham (Book).

Requirements
Must have
• I like the idea of white background on one side and solid color (blue, black, etc.) on back of card.

Would like to utilize the fonts in the logo (to the extent possible) so as to not have too many fonts on card.
Nice to have
• I think the roles (i.e., Acquisitions, Asset Management, etc.,...) is probably likely best placed on the back side of the card with the logo maybe. See attached current business card for content.

```html
<!DOCTYPE html>
<html lang="en">
<head>
<meta charset="utf-8">
<title>BRAMLEY Executive Recruiting – Business Card</title>
<link rel="stylesheet" href="https://fonts.googleapis.com/css2?family=Montserrat:wght@400;500&display=swap">
<style>
  :root {
    --page-bg: #2a2a2c;
    --card-white: #f7f7f8;
    --navy: #0c1424;
    --brand-blue: #2f6fa6;
    --band-blue: #245d8f;
    --role-blue: #3f86c4;
    --ink: #1f2328;
    --grey: #8a8d92;
    --light-grey: #b6b9be;
  }
  * { margin: 0; padding: 0; box-sizing: border-box; }
  html, body { width: 1200px; height: 900px; overflow: hidden; }
  body {
    background: var(--page-bg);
    font-family: "Montserrat", sans-serif;
    position: relative;
  }
  .card {
    position: absolute;
    left: 250px;
    width: 700px;
    height: 400px;
    overflow: hidden;
  }
  /* Back */
  .card-back { top: 30px; background: var(--navy); }
  .role-list {
    position: absolute;
    right: 56px;
    top: 48px;
    list-style: none;
    text-align: right;
    color: var(--role-blue);
    font-size: 15px;
    line-height: 22px;
    letter-spacing: 1.5px;
    text-transform: uppercase;
  }
  .back-wordmark {
    position: absolute;
    right: 56px;
    bottom: 56px;
    text-align: right;
  }
  .back-wordmark .brand-name { color: #ffffff; }
  .back-wordmark .brand-tagline { color: var(--grey); }

  .brand-name {
    font-weight: 500;
    font-size: 40px;
    letter-spacing: 12px;
    line-height: 1;
  }
  .brand-tagline {
    font-weight: 400;
    font-size: 15px;
    letter-spacing: 5px;
    margin-top: 6px;
  }

  /* Front */
  .card-front { top: 470px; background: var(--card-white); }
  .front-logo {
    position: absolute;
    left: 44px;
    top: 46px;
    display: flex;
    align-items: center;
  }
  .logo-square {
    width: 54px;
    height: 54px;
    background: var(--brand-blue);
  }
  .logo-divider {
    width: 1px;
    height: 64px;
    background: var(--light-grey);
    margin: 0 16px;
  }
  .front-logo .brand-name { color: var(--ink); }
  .front-logo .brand-tagline { color: var(--grey); }

  .contact-person {
    position: absolute;
    left: 150px;
    top: 176px;
  }
  .person-name {
    color: var(--brand-blue);
    font-size: 24px;
    font-weight: 500;
    font-variant: small-caps;
    letter-spacing: 1px;
  }
  .person-title { color: var(--ink); font-size: 15px; margin-top: 2px; }
  .contact-lines {
    list-style: none;
    margin-top: 22px;
    color: var(--ink);
    font-size: 15px;
    line-height: 22px;
  }
  .contact-lines .label {
    color: var(--brand-blue);
    display: inline-block;
    width: 18px;
  }
  .office-address {
    position: absolute;
    left: 460px;
    top: 178px;
    color: var(--ink);
    font-size: 15px;
    line-height: 20px;
    font-style: normal;
  }
  .base-band {
    position: absolute;
    left: 0;
    right: 0;
    bottom: 0;
    height: 40px;
    background: var(--band-blue);
  }
</style>
</head>
<body>
  <section class="card card-back" aria-label="Card back">
    <ul class="role-list">
      <li>Acquisitions</li>
      <li>Asset Management</li>
      <li>Banking</li>
      <li>Development</li>
      <li>Capital Markets</li>
      <li>Brokerage</li>
    </ul>
    <div class="back-wordmark">
      <div class="brand-name">BRAMLEY</div>
      <div class="brand-tagline">executive recruiting</div>
    </div>
  </section>

  <section class="card card-front" aria-label="Card front">
    <div class="front-logo">
      <div class="logo-square"></div>
      <div class="logo-divider"></div>
      <div>
        <div class="brand-name">BRAMLEY</div>
        <div class="brand-tagline">executive recruiting</div>
      </div>
    </div>

    <div class="contact-person">
      <div class="person-name">Jordan Hale</div>
      <div class="person-title">President</div>
      <ul class="contact-lines">
        <li><span class="label">M</span>555-014-2290</li>
        <li><span class="label">P</span>555-014-2290</li>
        <li><span class="label">E</span>jordan@bramleyrecruiting.com</li>
      </ul>
    </div>

    <address class="office-address">
      1840 Larkspur Lane<br>
      Fairview, Texas 75069<br>
      www.bramleyrecruiting.com
    </address>

    <div class="base-band"></div>
  </section>
</body>
</html>
```